M25 Billboard Advert Required Please

I need an advert for a motorway Billboard on the M25 , the advert should show the following in big letters:
GUTTER CLEANING
DALRYNFLUES.COM and a small logo off to the side (Our logo is attached)

The printer has requested the following (Important please) the advert has to be
pdf file / 300 dpi/landscape orientation / scaled to a minimum 25% advert size ( this particular site is 22ft x 10ft so 25% of this please). Please also make sure that the artwork is embedded and outlined correctly if this is incorrect it will affect the printing of the banner.

Target Market(s)

General Public

Industry/Entity Type

Gutter Cleaning

Requirements
Should not have
• No Change to our Logo

```html
<!DOCTYPE html>
<html lang="en">
<head>
<meta charset="utf-8">
<title>Dalryn Flues – Gutter Cleaning Billboard</title>
<link rel="stylesheet" href="https://fonts.googleapis.com/css2?family=Anton&family=Montserrat:wght@600;700&family=Open+Sans:wght@700&display=swap">
<style>
  :root {
    --stage: #6e6e6e;
    --paper: #f3f3f3;
    --paper-shade: #e4e4e4;
    --red: #e8291c;
    --red-deep: #d22418;
    --ink: #2a2d33;
    --white: #ffffff;
  }
  html, body {
    margin: 0;
    width: 1027px;
    height: 1200px;
    overflow: hidden;
    background: var(--stage);
  }
  .billboard {
    position: absolute;
    left: 33px;
    top: 382px;
    width: 960px;
    height: 436px;
    box-shadow: 0 6px 18px rgba(0,0,0,0.35);
  }
  .billboard svg { display: block; width: 960px; height: 436px; }
  .brand-name { font-family: "Montserrat", sans-serif; font-weight: 700; font-size: 30px; fill: var(--ink); }
  .brand-tagline { font-family: "Open Sans", sans-serif; font-weight: 700; font-size: 12px; fill: var(--ink); }
  .headline { font-family: "Anton", sans-serif; }
  .headline-top { fill: var(--red); }
  .headline-bottom { fill: var(--ink); }
  .service-label { font-family: "Montserrat", sans-serif; font-weight: 700; font-size: 17px; fill: var(--white); letter-spacing: 0.5px; }
  .website { font-family: "Montserrat", sans-serif; font-weight: 600; font-size: 24px; fill: var(--white); letter-spacing: 0.5px; }
  .quote-label { font-family: "Montserrat", sans-serif; font-weight: 600; font-size: 19px; fill: var(--white); letter-spacing: 0.5px; }
  .phone { font-family: "Anton", sans-serif; font-size: 50px; fill: var(--ink); }
  .icon-line { fill: none; stroke: var(--white); stroke-width: 1.6; stroke-linejoin: round; }
</style>
</head>
<body>
<div class="billboard">
  <svg viewBox="0 0 960 436" xmlns="http://www.w3.org/2000/svg">
    <defs>
      <linearGradient id="paperGrad" x1="0" y1="0" x2="1" y2="1">
        <stop offset="0" stop-color="var(--paper)"/>
        <stop offset="0.5" stop-color="#f7f7f7"/>
        <stop offset="1" stop-color="var(--paper-shade)"/>
      </linearGradient>
      <linearGradient id="photoGrad" x1="0" y1="0" x2="0.3" y2="1">
        <stop offset="0" stop-color="#b86a52"/>
        <stop offset="0.35" stop-color="#6b5244"/>
        <stop offset="0.7" stop-color="#5c6670"/>
        <stop offset="1" stop-color="#4f7a45"/>
      </linearGradient>
    </defs>

    <!-- base -->
    <rect class="base" width="960" height="436" fill="url(#paperGrad)"/>

    <!-- brand -->
    <g class="brand">
      <circle cx="208" cy="39" r="9" fill="var(--red)"/>
      <text class="brand-name" x="224" y="50">Dalryn Flues</text>
      <text class="brand-tagline" x="145" y="82">Clean gutters protect your property</text>
    </g>

    <!-- headline -->
    <text class="headline headline-top" x="73" y="208" font-size="128" textLength="368" lengthAdjust="spacingAndGlyphs">GUTTER</text>
    <text class="headline headline-bottom" x="73" y="302" font-size="96" textLength="368" lengthAdjust="spacingAndGlyphs">CLEANING</text>

    <!-- photo area -->
    <polygon role="img" aria-label="Photo of a gloved hand clearing leaves from a roof gutter below terracotta tiles" points="556,72 960,72 960,341 479,341" fill="url(#photoGrad)"/>
    <polygon class="accent-slash" points="536,140 544,140 502,264 494,264" fill="var(--red)"/>

    <!-- website band -->
    <polygon class="web-band" points="513,0 960,0 960,72 556,72" fill="var(--red)"/>
    <g class="globe-icon" fill="none" stroke="var(--white)" stroke-width="1.6">
      <circle cx="584" cy="40" r="11"/>
      <ellipse cx="584" cy="40" rx="5" ry="11"/>
      <line x1="573" y1="40" x2="595" y2="40"/>
      <line x1="575" y1="34" x2="593" y2="34"/>
      <line x1="575" y1="46" x2="593" y2="46"/>
    </g>
    <text class="website" x="606" y="49">www.DALRYNFLUES.COM</text>

    <!-- services band -->
    <polygon class="services-band" points="0,337 479,337 528,436 0,436" fill="var(--ink)"/>
    <line x1="262" y1="361" x2="262" y2="411" stroke="var(--white)" stroke-width="1.5"/>

    <g class="service-icon">
      <circle cx="135" cy="335" r="25" fill="var(--red)"/>
      <path class="icon-line" d="M123,336 L135,324 L147,336 M126,333 V348 H144 V333 M131,348 V340 H136 V348 M139,338 H143 V342 H139 Z"/>
    </g>
    <text class="service-label" text-anchor="middle" x="135" y="388">RESIDENTIAL</text>
    <text class="service-label" text-anchor="middle" x="135" y="409">SERVICES</text>

    <g class="service-icon">
      <circle cx="384" cy="335" r="25" fill="var(--red)"/>
      <path class="icon-line" d="M375,348 V323 H393 V348 Z M371,348 H397 M379,327 H381 M383,327 H385 M387,327 H389 M379,332 H381 M383,332 H385 M387,332 H389 M379,337 H381 M383,337 H385 M387,337 H389 M382,348 V342 H386 V348"/>
    </g>
    <text class="service-label" text-anchor="middle" x="384" y="388">COMMERCIAL</text>
    <text class="service-label" text-anchor="middle" x="384" y="409">SERVICES</text>

    <!-- quote call to action -->
    <polygon class="quote-tag" points="578,316 888,316 897,358 590,358" fill="var(--red)"/>
    <text class="quote-label" text-anchor="middle" x="738" y="344">FREE QUOTE REQUEST</text>
    <text class="phone" text-anchor="middle" x="742" y="412">0800 046 3170</text>
  </svg>
</div>
</body>
</html>
```